Professional Business Cards for Recruiting Company

We'd like professional 2-sided business cards that reflect a color scheme that matches our website, www.quillmerbay.com, and / or logo that is attached.

Slogan used is "We Know People", but needs to be editable because we change it up to "We Know Developers", "We Speak Geek", etc.

Must includes logo, slogan, first and last name, address, email, mobile number and website address.

Files attached for ideas.

Thanks!

Contact Information for Business Card

Logo, Company name, First name, Last name, addresss, email, phone, website address.

Font styles to use
Sans Serif

Colors
0054AA
0677BA
7BADD7
CADEEF
E8F1F8

Requirements
Nice to have
• I do like the following designs. 22962062 and 22962651. Couple ideas anyway.

```html
<!DOCTYPE html>
<html lang="en">
<head>
<meta charset="utf-8">
<title>Quillmerbay Business Card</title>
<link href="https://fonts.googleapis.com/css2?family=Poppins:wght@300;400;500&display=swap" rel="stylesheet">
<style>
  :root {
    --stage: #878787;
    --brand-blue: #1a4a98;
    --pattern-blue: #1c4d9f;
    --pattern-deep: #17438c;
    --ink: #2a2a2a;
    --muted: #7a7a7a;
    --paper: #ffffff;
  }
  * { margin: 0; padding: 0; box-sizing: border-box; }
  html, body { width: 1075px; height: 1200px; overflow: hidden; }
  body {
    background: var(--stage);
    font-family: "Poppins", sans-serif;
    position: relative;
  }
  .card {
    position: absolute;
    left: 205px;
    width: 663px;
    height: 395px;
    overflow: hidden;
  }
  .card--front { top: 187px; }
  .card--back { top: 648px; background: var(--paper); }

  .front-pattern {
    position: absolute; inset: 0;
    background: linear-gradient(135deg, var(--pattern-blue), var(--pattern-deep));
  }
  .front-brand {
    position: absolute;
    left: 292px; top: 234px;
    display: flex; align-items: center; gap: 16px;
  }
  .brand-square {
    width: 34px; height: 34px;
    border: 2px solid currentColor;
  }
  .front-brand { color: var(--paper); }
  .front-brand .brand-name {
    font-size: 34px; font-weight: 300; letter-spacing: 1px;
  }

  .back-brand {
    position: absolute;
    left: 50px; top: 180px;
    display: flex; align-items: center; gap: 12px;
    color: var(--brand-blue);
  }
  .back-brand .brand-square { width: 26px; height: 26px; }
  .back-brand .brand-name { font-size: 24px; font-weight: 300; letter-spacing: 0.5px; }

  .divider {
    position: absolute;
    left: 336px; top: 106px;
    width: 2px; height: 183px;
    background: var(--brand-blue);
  }
  .contact {
    position: absolute;
    left: 355px; top: 100px;
    color: var(--ink);
  }
  .contact__name {
    font-size: 23px; font-weight: 400; line-height: 1.2; letter-spacing: 0.3px;
  }
  .contact__first { color: var(--brand-blue); }
  .contact__last { color: var(--muted); }
  .contact__role { font-size: 15px; margin-top: 2px; margin-left: 2px; }
  .contact__lines { list-style: none; margin-top: 12px; font-size: 17px; line-height: 22px; }
  .contact__lines li { display: flex; align-items: center; gap: 6px; }
  .contact__lines svg { width: 16px; height: 16px; fill: var(--brand-blue); flex: none; }
  .contact__address { margin-top: 12px; font-size: 17px; line-height: 22px; }

  .slogan-band {
    position: absolute;
    left: 0; bottom: 0;
    width: 100%; height: 53px;
    background: var(--brand-blue);
    color: var(--paper);
    display: flex; align-items: center; justify-content: center;
    font-size: 17px; font-weight: 500; letter-spacing: 0.3px;
  }
</style>
</head>
<body>
  <section class="card card--front">
    <div class="front-pattern" role="img" aria-label="Embossed repeating monogram pattern in tonal blue"></div>
    <div class="front-brand">
      <span class="brand-square"></span>
      <span class="brand-name">QUILLMERBAY</span>
    </div>
  </section>

  <section class="card card--back">
    <div class="back-brand">
      <span class="brand-square"></span>
      <span class="brand-name">QUILLMERBAY</span>
    </div>
    <div class="divider"></div>
    <div class="contact">
      <p class="contact__name"><span class="contact__first">DANIEL</span> <span class="contact__last">HARWICK</span></p>
      <p class="contact__role">MANAGING DIRECTOR</p>
      <ul class="contact__lines">
        <li><svg viewBox="0 0 24 24"><path d="M6.6 10.8a15.1 15.1 0 0 0 6.6 6.6l2.2-2.2a1 1 0 0 1 1-.25 11.4 11.4 0 0 0 3.6.57 1 1 0 0 1 1 1V20a1 1 0 0 1-1 1A17 17 0 0 1 3 4a1 1 0 0 1 1-1h3.5a1 1 0 0 1 1 1c0 1.25.2 2.45.57 3.57a1 1 0 0 1-.25 1z"/></svg>044-987 654 321</li>
        <li><svg viewBox="0 0 24 24"><path d="M2 5h20v14H2z M2 5l10 8 10-8" fill="none" stroke="#1a4a98" stroke-width="0"/><path d="M2 5h20l-10 8z"/><path d="M2 7l10 8 10-8v12H2z"/></svg>info@quillmerbay.com</li>
        <li><svg viewBox="0 0 24 24"><path d="M12 2a10 10 0 1 0 0 20 10 10 0 0 0 0-20zm-1 2.1V8H7.5A8 8 0 0 1 11 4.1zm2 0A8 8 0 0 1 16.5 8H13zM6.6 10H11v4H6.6a8 8 0 0 1 0-4zm6.4 0h4.4a8 8 0 0 1 0 4H13zm-5.5 6H11v3.9A8 8 0 0 1 7.5 16zm5.5 0h3.5a8 8 0 0 1-3.5 3.9z"/></svg>www.quillmerbay.com</li>
      </ul>
      <p class="contact__address">421, Address line goes here<br>45452,Country Name</p>
    </div>
    <div class="slogan-band">WE KNOW PEOPLE</div>
  </section>
</body>
</html>
```